I need 2 flyers designed for my business

Both can be similar in design and will have different purposes. I need an education based flyer and I need a government based flyer. The focus of the flyer will be software on the front and services on the back.
These all need to be 8.5x 11 in dimension (they can be full bleed). I would like to be able to print these out if needed. The design needs to look good with our website > www.brelmark.com

The software details are on the website.

```html
<!DOCTYPE html>
<html lang="en">
<head>
<meta charset="utf-8">
<title>Brelmark Flyers</title>
<link rel="stylesheet" href="https://fonts.googleapis.com/css2?family=Poppins:wght@300;600;700&family=Roboto:wght@400;500;700&display=swap">
<style>
:root{
  --bg:#a3a8ac;
  --red:#8b1a22;
  --red-deep:#6e0f1e;
  --olive:#8a7a32;
  --olive-dark:#7a6c2b;
  --white:#ffffff;
  --paper:#f3f3f4;
  --text:#4a4a4a;
}
*{margin:0;padding:0;box-sizing:border-box}
html,body{width:1200px;height:1200px;overflow:hidden;background:var(--bg)}
body{position:relative;font-family:'Roboto',sans-serif}
.flyer{position:absolute;top:293px;width:502px;height:650px;background:var(--white);overflow:hidden;box-shadow:2px 3px 6px rgba(0,0,0,.35)}
.flyer--software{left:78px}
.flyer--services{left:620px}
.abs{position:absolute}
.hero{position:absolute;left:0;top:0}
.brand{position:absolute;display:flex;align-items:center;gap:7px;font-family:'Roboto',sans-serif;font-weight:700;color:var(--red);font-size:22px;letter-spacing:1px}
.brand__mark{width:18px;height:18px;background:var(--red)}
.hero-title{position:absolute;font-family:'Poppins',sans-serif;font-weight:700;color:var(--white);font-size:27px;line-height:30px}
.hero-sub{position:absolute;font-family:'Poppins',sans-serif;font-weight:300;color:var(--white);font-size:12.5px;line-height:16px}
.band-title{position:absolute;font-family:'Poppins',sans-serif;font-weight:700;color:var(--white);font-size:15.5px;line-height:19px}
.intro{position:absolute;left:40px;top:350px;width:430px;font-size:7.8px;line-height:10px;color:var(--text)}
.intro p{margin-bottom:6px}
.steps{position:absolute;left:0;top:469px;width:502px;height:134px;background:var(--red)}
.steps__tab{position:absolute;left:71px;top:0;width:354px;height:25px;background:var(--olive);clip-path:polygon(0 0,100% 0,95% 100%,5% 100%);color:var(--white);font-family:'Poppins',sans-serif;font-weight:600;font-size:12.5px;text-align:center;line-height:25px}
.steps__lead{position:absolute;top:36px;width:100%;text-align:center;color:var(--white);font-size:8px}
.step{position:absolute;top:55px;width:110px;text-align:center;color:var(--white);font-size:7.8px;line-height:10px}
.step__label{display:inline-block;background:var(--olive);border-radius:8px;padding:1px 7px;font-weight:500;font-size:10px;line-height:14px;margin-bottom:4px}
.step-rule{position:absolute;top:61px;width:1px;height:64px;background:var(--white)}
.contact{position:absolute;left:0;top:603px;width:502px;height:47px}
.contact__label{position:absolute;left:20px;top:14px;color:var(--red);font-weight:700;font-size:15px}
.contact__pill{position:absolute;left:109px;top:4px;width:393px;height:40px;background:var(--olive);border-radius:20px 0 0 20px}
.contact__phone{position:absolute;left:37px;top:8px;color:var(--white);font-weight:500;font-size:19px;display:flex;align-items:center;gap:8px}
.contact__info{position:absolute;left:200px;top:8px;color:var(--white);font-size:7.8px;line-height:14px}
.contact__info span{display:flex;align-items:center;gap:5px}
.service{position:absolute;left:0;width:502px;height:93px}
.service--alt{background:var(--paper)}
.service__head{position:absolute;left:0;top:0;width:185px;height:93px;border-radius:0 46px 46px 0;z-index:2}
.service__icon{position:absolute;left:27px;top:22px;width:50px;height:50px;border-radius:50%;background:var(--olive);display:flex;align-items:center;justify-content:center}
.service__title{position:absolute;left:94px;top:18px;color:var(--white);font-weight:500;font-size:13.5px;line-height:16.5px}
.service__desc{position:absolute;left:165px;top:0;width:162px;height:93px;background:#ececed;border-radius:0 46px 46px 0;padding:20px 14px 0 33px;font-size:7.8px;line-height:10px;color:var(--text)}
.service--alt .service__desc{background:#e4e4e6}
.service__list{position:absolute;left:345px;top:17px;width:150px;font-size:7px;line-height:9px;color:var(--text)}
.service__list h4{color:var(--red);font-size:8.5px;font-weight:700;margin-bottom:4px}
.service__list li{list-style:none;position:relative;padding-left:9px;margin-bottom:2px}
.service__list li::before{content:"";position:absolute;left:0;top:2px;width:5px;height:5px;border-radius:50%;background:var(--red)}
.sales{position:absolute;left:0;top:601px;width:502px;height:49px;background:var(--olive)}
.sales__label{position:absolute;left:28px;top:14px;color:var(--white);font-weight:500;font-size:15.5px}
.sales__pill{position:absolute;left:164px;top:5px;width:338px;height:40px;background:var(--red);border-radius:20px 0 0 20px;display:flex;align-items:center;gap:18px;padding-left:12px;color:var(--white);font-weight:500;font-size:15.5px}
.sales__pill span{display:flex;align-items:center;gap:8px}
.dot{width:14px;height:14px;border-radius:50%;background:var(--white)}
</style>
</head>
<body>

<section class="flyer flyer--software">
  <svg class="hero" width="502" height="337" viewBox="0 0 502 337">
    <defs>
      <linearGradient id="laptopPhoto" x1="0" y1="0" x2="1" y2="1">
        <stop offset="0" stop-color="#5c6578"/>
        <stop offset=".55" stop-color="#1f2d6b"/>
        <stop offset="1" stop-color="#2a3f86"/>
      </linearGradient>
    </defs>
    <rect x="0" y="288" width="502" height="49" fill="var(--red)"/>
    <path d="M175,337 Q200,0 420,0 L502,0 L502,337 Z" fill="var(--red)"/>
    <g role="img" aria-label="Photo of hands typing on a laptop with floating digital documents">
      <path d="M200,325 Q225,24 430,22 L502,22 L502,325 Z" fill="url(#laptopPhoto)"/>
    </g>
    <path d="M0,88 H227 A98.5,98.5 0 0 1 227,285 H0 Z" fill="var(--olive)" opacity=".96" stroke="var(--white)" stroke-width="4"/>
  </svg>
  <div class="brand" style="left:40px;top:30px"><i class="brand__mark"></i>BRELMARK</div>
  <h1 class="hero-title" style="left:40px;top:101px">Record<br>Management<br>Services &amp;<br>Software</h1>
  <p class="hero-sub" style="left:40px;top:233px">Spend time using your information<br>instead of searching for it.</p>
  <h2 class="band-title" style="left:40px;top:294px">Your Lost Records<br>Problem, Solved</h2>

  <div class="intro">
    <p>You need a partner you can count on when it comes to your records – one that can shoulder the load and come through for you quickly. Brelmark wants to be that partner for you.</p>
    <p>We use our records management expertise to solve your problems, so you can focus your attention on your business.</p>
    <p>We’re prepared to journey with you for the long-haul as trustworthy team members. That means anytime new needs arise, we’ll be by your side with new solutions every time.</p>
    <p>Brelmark Advantage Solution: Once we pick up and box your records, we safeguard them so you can access them anytime – at no cost – without ever worrying about their whereabouts.</p>
  </div>

  <div class="steps">
    <div class="steps__tab">How to Go Paperless with Brelmark</div>
    <p class="steps__lead">Choose Brelmark to get a document solution tailored to your needs.</p>
    <div class="step" style="left:21px"><span class="step__label">Get Your Quote</span><br>Fill out our online form,<br>and we’ll give you a call.<br>We’ll hear your needs<br>and deliver a price.</div>
    <i class="step-rule" style="left:135px"></i>
    <div class="step" style="left:139px"><span class="step__label">Love Your Terms</span><br>We strive to save you<br>time and money with<br>terms that are win-win –<br>and keep this process<br>simple.</div>
    <i class="step-rule" style="left:253px"></i>
    <div class="step" style="left:257px"><span class="step__label">Implement Plan</span><br>We’ll handle everything<br>your project needs and<br>train you on our<br>easy-to-use software.</div>
    <i class="step-rule" style="left:371px"></i>
    <div class="step" style="left:375px"><span class="step__label">Be Free Of Paper</span><br>Once you’re paperless,<br>we don’t just go away.<br>We secure your docs<br>and provide 24/7<br>ongoing support.</div>
  </div>

  <div class="contact">
    <span class="contact__label">Contact Us</span>
    <div class="contact__pill">
      <div class="contact__phone" style="left:10px">
        <svg width="20" height="20" viewBox="0 0 20 20"><circle cx="10" cy="10" r="10" fill="var(--white)"/><path d="M6.5,5 L8.5,5 L9.3,7.8 L8,8.8 Q9.2,11.2 11.3,12 L12.3,10.8 L15,11.6 L15,13.6 Q14.5,15 13,15 Q6,14 5.2,6.8 Q5.2,5 6.5,5Z" fill="var(--red)"/></svg>
        (555) 318-2046
      </div>
      <div class="contact__info">
        <span><svg width="7" height="9" viewBox="0 0 7 9"><path d="M3.5,0 A3.5,3.5 0 0 1 7,3.5 C7,6 3.5,9 3.5,9 C3.5,9 0,6 0,3.5 A3.5,3.5 0 0 1 3.5,0Z" fill="var(--white)"/><circle cx="3.5" cy="3.5" r="1.3" fill="var(--olive)"/></svg>214 Commerce Drive Fairview, Ohio 44000</span>
        <span><svg width="8" height="8" viewBox="0 0 8 8"><circle cx="4" cy="4" r="3.4" fill="none" stroke="var(--white)"/><path d="M0.6,4 H7.4 M4,0.6 V7.4" stroke="var(--white)" stroke-width=".8"/></svg>www.brelmark.com</span>
      </div>
    </div>
  </div>
</section>

<section class="flyer flyer--services">
  <svg class="hero" width="502" height="316" viewBox="0 0 502 316">
    <defs>
      <linearGradient id="buildingPhoto" x1="0" y1="0" x2="1" y2="1">
        <stop offset="0" stop-color="#d8dde2"/>
        <stop offset=".5" stop-color="#8f9aa6"/>
        <stop offset="1" stop-color="#5f6c7a"/>
      </linearGradient>
    </defs>
    <path d="M160,316 Q185,0 420,0 L502,0 L502,316 Z" fill="var(--red)"/>
    <g role="img" aria-label="Photo of a columned government building with a flag">
      <path d="M175,303 Q200,12 430,10 L502,10 L502,303 Z" fill="url(#buildingPhoto)"/>
    </g>
    <path d="M0,116 H213 A98.5,98.5 0 0 1 213,313 H0 Z" fill="var(--olive)" opacity=".96" stroke="var(--white)" stroke-width="4"/>
  </svg>
  <div class="brand" style="left:35px;top:46px"><i class="brand__mark"></i>BRELMARK</div>
  <h1 class="hero-title" style="left:27px;top:140px;font-family:'Roboto',sans-serif;font-size:39px;line-height:45px">The Leader<br>In Records<br>Management</h1>

  <div class="service" style="top:316px">
    <div class="service__head" style="background:var(--red)">
      <div class="service__icon"><svg width="30" height="28" viewBox="0 0 30 28" fill="none" stroke="var(--white)" stroke-width="1.5"><path d="M15,2 L28,9 L15,16 L2,9 Z"/><path d="M2,14 L15,21 L28,14"/><path d="M2,19 L15,26 L28,19"/></svg></div>
      <div class="service__title">Document<br>Scanning<br>Services</div>
    </div>
    <div class="service__desc">Fast, efficient process for the conversion of existing paper records to digital archives, increasing access and reducing onsite storage and costs.</div>
    <div class="service__list"><h4>Scanning services for any format:</h4><ul><li>Standard Office Documents</li><li>16mm, 35mm Roll Microfilm</li><li>Microfiche (Jackets or COM)</li><li>Large Format Documents/Drawings</li></ul></div>
  </div>

  <div class="service service--alt" style="top:410px">
    <div class="service__head" style="background:var(--red-deep)">
      <div class="service__icon"><svg width="24" height="30" viewBox="0 0 24 30" fill="none" stroke="var(--white)" stroke-width="1.5"><path d="M6,13 V8 A6,6 0 0 1 18,8 V10"/><rect x="2" y="13" width="20" height="15" rx="1.5"/><rect x="10" y="17" width="4" height="6" rx="2"/></svg></div>
      <div class="service__title">Document<br>Storage<br>Services</div>
    </div>
    <div class="service__desc">Solution for offsite document storage and retrieval to effectively store, manage, and safeguard your vital business records and documents.</div>
    <div class="service__list"><h4>A local, convenient solution:</h4><ul><li>Free Up Office Space</li><li>Reduce Costs</li><li>Keep Records in a Fireproof, Waterproof &amp; Wind-Safe Facility</li></ul></div>
  </div>

  <div class="service" style="top:504px">
    <div class="service__head" style="background:var(--red)">
      <div class="service__icon"><svg width="28" height="28" viewBox="0 0 28 28" fill="none" stroke="var(--white)" stroke-width="1.5"><rect x="2" y="3" width="24" height="6"/><rect x="4" y="9" width="20" height="17"/><rect x="9" y="14" width="10" height="6"/><path d="M11,17 H17"/></svg></div>
      <div class="service__title">Secure<br>Document<br>Shredding</div>
    </div>
    <div class="service__desc">Safely and cost-effectively destroy unnecessary paperbased documents. One-time or recurring, our solutions are tailored to you.</div>
    <div class="service__list"><h4>Destroy Unnecessary Documents:</h4><ul><li>Protect confidential information</li><li>Reduce the cost of managing information that is no longer useful</li><li>Ensure compliance with regulations for information destruction</li></ul></div>
  </div>

  <div class="sales">
    <span class="sales__label">Sales inquiries to</span>
    <div class="sales__pill">
      <span><i class="dot"></i>(555) 402-7731</span>
      <span><i class="dot"></i>help@brelmark.com</span>
    </div>
  </div>
</section>

</body>
</html>
```